TIDAL VERGE needs bisness cards pronto

Bisness name is "TIDAL VERGE" new bisness the bisness includes lawn mowing, garden matanace, and any jobs around the house.
I need a card that is colorful and vibrant and the bisness of lawn mowing maybe with some nature with it. It also needs my contact details"Darren Quellby mobile 0413562049 call for free quote and email norma.vance@fernmail.com.au and a catchy tag line

Industry/Entity Type

House

Requirements
Must have
• Bisness name "TIDAL VERGE"
Contact details "0413562049"
Email norma.vance@fernmail.com.au
Call for free quote

```html
<!DOCTYPE html>
<html lang="en">
<head>
<meta charset="utf-8">
<title>Tidal Verge – Business Card</title>
<link rel="stylesheet" href="https://fonts.googleapis.com/css2?family=Fira+Sans:wght@400&display=swap">
<style>
  :root {
    --backdrop-dark: #08701a;
    --backdrop-mid: #0a9414;
    --backdrop-light: #0bb50e;
    --grass-deep: #2f7424;
    --grass-mid: #3f8c30;
    --grass-light: #5aa647;
    --band-white: #ffffff;
    --ink-green: #0c5a1c;
    --label-white: #ffffff;
  }
  * { box-sizing: border-box; margin: 0; padding: 0; }
  html, body { width: 1200px; height: 900px; overflow: hidden; }
  body {
    position: relative;
    font-family: "Fira Sans", sans-serif;
    background: linear-gradient(115deg, var(--backdrop-dark) 0%, var(--backdrop-mid) 45%, var(--backdrop-light) 100%);
  }
  .side-label {
    position: absolute;
    color: var(--label-white);
    font-size: 40px;
    font-weight: 400;
    line-height: 1;
  }
  .side-label--front { left: 817px; top: 48px; }
  .side-label--back { left: 313px; top: 808px; }

  .card {
    position: absolute;
    width: 710px;
    height: 368px;
    border-radius: 15px;
    overflow: hidden;
    box-shadow: 2px 3px 6px rgba(0, 0, 0, 0.35);
  }
  .card--front { left: 85px; top: 38px; }
  .card--back { left: 440px; top: 477px; }

  .grass {
    position: absolute;
    inset: 0;
    background:
      radial-gradient(circle at 20% 30%, var(--grass-light) 0%, transparent 40%),
      radial-gradient(circle at 75% 70%, var(--grass-light) 0%, transparent 45%),
      radial-gradient(circle at 60% 20%, var(--grass-deep) 0%, transparent 40%),
      linear-gradient(160deg, var(--grass-mid), var(--grass-deep));
  }

  .front-brand {
    position: absolute;
    left: 0; right: 0;
    top: 160px;
    display: flex;
    flex-direction: column;
    align-items: center;
  }
  .front-brand__dot {
    width: 44px; height: 44px;
    border-radius: 50%;
    background: var(--ink-green);
    margin-bottom: 36px;
  }
  .front-brand__name {
    color: var(--label-white);
    font-size: 64px;
    font-weight: 400;
    letter-spacing: 6px;
    line-height: 1;
  }
  .front-brand__tagline {
    margin-top: 18px;
    color: var(--label-white);
    font-size: 24px;
    font-weight: 400;
    letter-spacing: 1px;
    line-height: 1;
  }

  .info-band {
    position: absolute;
    left: 0; right: 0;
    top: 83px;
    height: 200px;
    background: var(--band-white);
  }
  .info-band__brand {
    position: absolute;
    left: 40px;
    top: 0; bottom: 0;
    width: 200px;
    display: flex;
    align-items: center;
    justify-content: center;
    color: var(--ink-green);
    font-size: 26px;
    font-weight: 400;
    letter-spacing: 1px;
  }
  .contact {
    position: absolute;
    left: 286px;
    top: 26px;
    list-style: none;
    color: var(--ink-green);
    font-size: 26px;
    font-weight: 400;
    line-height: 37px;
  }
</style>
</head>
<body>
  <span class="side-label side-label--front">Front</span>
  <span class="side-label side-label--back">Back</span>

  <section class="card card--front">
    <div class="grass" role="img" aria-label="Close-up photo of freshly mown green lawn"></div>
    <div class="front-brand">
      <span class="front-brand__dot"></span>
      <h1 class="front-brand__name">TIDAL VERGE</h1>
      <p class="front-brand__tagline">Sharp edges, happy gardens</p>
    </div>
  </section>

  <section class="card card--back">
    <div class="grass" role="img" aria-label="Close-up photo of freshly mown green lawn"></div>
    <div class="info-band">
      <div class="info-band__brand">TIDAL VERGE</div>
      <ul class="contact">
        <li>Darren Quellby</li>
        <li>0413562049</li>
        <li>Call for free quote</li>
        <li>norma.vance@fernmail.com.au</li>
      </ul>
    </div>
  </section>
</body>
</html>
```